Verpackungsdesign für Lifestyle-Diagnostik und Supplements im Bereich Longevity
Zielgruppe
Wir machen Lifestyle-Diagnostik und Supplements im Bereich Longevity
Aufgabenstellung
Verpackung eines Tests (wie der hier: https://shop.quellmora.com/products/zentrip) in der gezeigten Metallschachtel, Supplements in den gezeigten Dosen. Ein Set besteht aus einem Test und zwei Dosen (morgens und abends). Farbschema und Logo Korunelle wie im Anhang. paar Details zu den Supplements auch in den Dateien
Bitte auch an Prägung und anderen Gestaltungsmöglichkeiten denken

```html
<!DOCTYPE html>
<html lang="de">
<head>
<meta charset="utf-8">
<title>Korunelle – Verpackungsset Longevity</title>
<link rel="stylesheet" href="https://fonts.googleapis.com/css2?family=Barlow+Condensed:wght@600;700&family=Roboto:wght@400;500;700&display=swap">
<style>
  :root {
    --teal: #134a4e;
    --green: #9dc43b;
    --green-light: #b9d867;
    --ink: #2f3a3b;
    --muted: #8a9394;
    --paper: #ffffff;
    --stage: #ececec;
  }
  * { box-sizing: border-box; margin: 0; padding: 0; }
  html, body { width: 1200px; height: 2258px; overflow: hidden; }
  body {
    background: var(--stage);
    font-family: "Roboto", Arial, sans-serif;
    color: var(--ink);
    position: relative;
  }

  /* ---------- tin label ---------- */
  .label {
    position: absolute;
    top: 110px;
    width: 540px;
    height: 684px;
    background: var(--paper);
    overflow: hidden;
    box-shadow: 0 6px 24px rgba(0,0,0,.12);
  }
  .label--am { left: 40px; }
  .label--pm { left: 620px; }

  .brand {
    position: absolute;
    left: 0; right: 0;
    text-align: center;
  }
  .brand__name {
    font-family: "Roboto", Arial, sans-serif;
    font-weight: 700;
    color: var(--teal);
    line-height: 1;
  }
  .brand__tagline {
    font-size: 9px;
    color: var(--green);
    margin-top: 3px;
    font-weight: 500;
  }
  .label .brand { top: 62px; }
  .label .brand__name { font-size: 20px; }

  .product-title {
    position: absolute;
    left: 48px; top: 128px;
    display: flex; align-items: center; gap: 4px;
    font-family: "Barlow Condensed", "Arial Narrow", sans-serif;
    font-weight: 700;
    font-size: 88px;
    line-height: 1;
  }
  .product-title__icon {
    width: 72px; height: 62px;
    background: var(--teal);
    border-radius: 31px 6px 6px 31px;
    display: flex; align-items: center; justify-content: center;
    margin-right: 2px;
  }
  .product-title__time { color: var(--green); }
  .product-title__word { color: var(--teal); margin-left: 10px; }

  .benefit-pills {
    position: absolute;
    left: 48px; top: 221px;
    display: flex; gap: 12px;
  }
  .pill {
    width: 214px; height: 34px;
    border: 1.5px solid #cfd6d2;
    border-radius: 17px;
    display: flex; align-items: center;
    padding-left: 8px;
    color: var(--green);
    font-size: 17px;
  }
  .pill__icon {
    width: 24px; height: 24px;
    border-radius: 50%;
    background: #eef1ef;
    display: flex; align-items: center; justify-content: center;
    flex: none;
  }
  .pill__text { flex: 1; text-align: center; padding-right: 12px; }

  .benefits {
    position: absolute;
    left: 63px; top: 305px;
    list-style: none;
  }
  .benefits li {
    display: flex; align-items: center; gap: 12px;
    height: 41px;
    font-size: 14px;
    color: var(--ink);
  }
  .tick { flex: none; }

  .count {
    position: absolute;
    left: 56px; top: 452px;
    color: var(--green);
    font-family: "Barlow Condensed", "Arial Narrow", sans-serif;
    font-weight: 700;
    font-size: 86px;
    line-height: 1;
  }
  .count__unit {
    position: absolute;
    left: 58px; top: 536px;
    font-size: 13px;
    font-weight: 700;
    letter-spacing: .5px;
    color: var(--teal);
  }

  .footer-band {
    position: absolute;
    left: 0; bottom: 0;
    width: 540px; height: 141px;
  }
  .footer-band__shape { position: absolute; left: 0; top: 0; }
  .intake {
    position: absolute;
    left: 44px; bottom: 38px;
    display: flex; align-items: center; gap: 8px;
    color: #fff;
    font-size: 14px;
  }
  .intake__icon { flex: none; display: block; }
  .complex {
    position: absolute;
    left: 300px; top: 34px;
    width: 215px;
    color: #fff;
  }
  .complex__title { font-size: 14px; font-weight: 700; margin-bottom: 10px; }
  .complex__text { font-size: 10px; line-height: 1.45; }

  /* ---------- diagnostic tin lid ---------- */
  .lid {
    position: absolute;
    left: 240px; top: 884px;
    width: 720px; height: 1063px;
    background: var(--paper);
    overflow: hidden;
    box-shadow: 0 6px 24px rgba(0,0,0,.12);
  }
  .lid__texture {
    position: absolute;
    inset: 0;
    background: linear-gradient(180deg, #f2f3f2 0%, #f8f8f8 35%, rgba(255,255,255,0) 58%);
  }
  .lid .brand {
    top: 560px; left: 98px; right: auto;
    width: 140px;
  }
  .lid .brand__name { font-size: 24px; }
  .lid__title {
    position: absolute;
    left: 95px; top: 626px;
    font-family: "Barlow Condensed", "Arial Narrow", sans-serif;
    font-weight: 700;
    font-size: 92px;
    line-height: 0.92;
  }
  .lid__title-top { color: var(--green); display: block; }
  .lid__title-bottom { color: var(--teal); display: block; }
  .lid__band {
    position: absolute;
    left: 0; bottom: 0;
    width: 720px; height: 228px;
  }
  .lid__band-shape { position: absolute; left: 0; top: 0; }
  .lid__claim {
    position: absolute;
    left: 100px; top: 38px;
    color: #fff;
    font-size: 21px;
    line-height: 1.2;
  }
</style>
</head>
<body>

  <section class="label label--am" aria-label="AM Formel Dosenetikett">
    <div class="brand">
      <div class="brand__name">Korunelle</div>
      <div class="brand__tagline">Täglicher Baustein Zukunft</div>
    </div>

    <h1 class="product-title">
      <span class="product-title__icon">
        <svg width="34" height="34" viewBox="0 0 34 34" fill="none" stroke="#fff" stroke-width="2.6" stroke-linecap="round">
          <circle cx="17" cy="17" r="6.5" fill="#fff"/>
          <path d="M17 2v4M17 28v4M2 17h4M28 17h4M6.4 6.4l2.8 2.8M24.8 24.8l2.8 2.8M6.4 27.6l2.8-2.8M24.8 9.2l2.8-2.8"/>
        </svg>
      </span>
      <span class="product-title__time">AM</span>
      <span class="product-title__word">FORMEL</span>
    </h1>

    <div class="benefit-pills">
      <div class="pill">
        <span class="pill__icon"><svg width="12" height="16" viewBox="0 0 12 16"><path d="M7 0L0 9h5l-1 7 7-9H6z" fill="#134a4e"/></svg></span>
        <span class="pill__text">Tägliche Energiev</span>
      </div>
      <div class="pill">
        <span class="pill__icon"><svg width="14" height="12" viewBox="0 0 14 12"><rect width="14" height="12" rx="2" fill="#134a4e"/><path d="M2 7h3l1.5-3 2 5 1.5-2h2" stroke="#fff" stroke-width="1.2" fill="none"/></svg></span>
        <span class="pill__text">Zellaktivierung</span>
      </div>
    </div>

    <ul class="benefits">
      <li><svg class="tick" width="24" height="24" viewBox="0 0 24 24"><circle cx="12" cy="12" r="12" fill="#9dc43b"/><path d="M6.5 12.5l3.5 3.5 7.5-8" stroke="#fff" stroke-width="2.6" fill="none" stroke-linecap="round" stroke-linejoin="round"/></svg>Unterstützt die Tagesenergie</li>
      <li><svg class="tick" width="24" height="24" viewBox="0 0 24 24"><circle cx="12" cy="12" r="12" fill="#9dc43b"/><path d="M6.5 12.5l3.5 3.5 7.5-8" stroke="#fff" stroke-width="2.6" fill="none" stroke-linecap="round" stroke-linejoin="round"/></svg>Mitochondriale Aktivierung</li>
      <li><svg class="tick" width="24" height="24" viewBox="0 0 24 24"><circle cx="12" cy="12" r="12" fill="#9dc43b"/><path d="M6.5 12.5l3.5 3.5 7.5-8" stroke="#fff" stroke-width="2.6" fill="none" stroke-linecap="round" stroke-linejoin="round"/></svg>Hilft, biologische Rhythmen zu regulieren</li>
    </ul>

    <div class="count">30</div>
    <div class="count__unit">KAPSELN</div>

    <div class="footer-band">
      <svg class="footer-band__shape" width="540" height="141" viewBox="0 0 540 141">
        <rect x="0" y="47" width="540" height="94" fill="#134a4e"/>
        <path d="M232 141 L262 30 Q270 0 305 0 L540 0 L540 141 Z" fill="#9dc43b"/>
      </svg>
      <div class="intake">
        <svg class="intake__icon" width="18" height="18" viewBox="0 0 34 34" fill="none" stroke="#fff" stroke-width="3" stroke-linecap="round"><circle cx="17" cy="17" r="6.5" fill="#fff"/><path d="M17 2v4M17 28v4M2 17h4M28 17h4M6.4 6.4l2.8 2.8M24.8 24.8l2.8 2.8M6.4 27.6l2.8-2.8M24.8 9.2l2.8-2.8"/></svg>
        <span>Morgens einnehmen</span>
      </div>
      <div class="complex">
        <div class="complex__title">Morgen-Nährstoffkomplex</div>
        <p class="complex__text">Formuliert zur Unterstützung der zellulären Energieproduktion und zur Förderung optimaler Morgenenergie.</p>
      </div>
    </div>
  </section>

  <section class="label label--pm" aria-label="PM Formel Dosenetikett">
    <div class="brand">
      <div class="brand__name">Korunelle</div>
      <div class="brand__tagline">Täglicher Baustein Zukunft</div>
    </div>

    <h1 class="product-title">
      <span class="product-title__icon">
        <svg width="34" height="34" viewBox="0 0 34 34">
          <path d="M20 4a13 13 0 1 0 10 19A11 11 0 0 1 20 4z" fill="#fff"/>
          <path d="M25 6v6M22 9h6" stroke="#fff" stroke-width="2" stroke-linecap="round"/>
        </svg>
      </span>
      <span class="product-title__time">PM</span>
      <span class="product-title__word">FORMEL</span>
    </h1>

    <div class="benefit-pills">
      <div class="pill">
        <span class="pill__icon"><svg width="12" height="16" viewBox="0 0 12 16"><path d="M7 0L0 9h5l-1 7 7-9H6z" fill="#134a4e"/></svg></span>
        <span class="pill__text">Regeneration</span>
      </div>
      <div class="pill">
        <span class="pill__icon"><svg width="14" height="12" viewBox="0 0 14 12"><rect width="14" height="12" rx="2" fill="#134a4e"/><path d="M2 7h3l1.5-3 2 5 1.5-2h2" stroke="#fff" stroke-width="1.2" fill="none"/></svg></span>
        <span class="pill__text">Zellreparatur</span>
      </div>
    </div>

    <ul class="benefits">
      <li><svg class="tick" width="24" height="24" viewBox="0 0 24 24"><circle cx="12" cy="12" r="12" fill="#9dc43b"/><path d="M6.5 12.5l3.5 3.5 7.5-8" stroke="#fff" stroke-width="2.6" fill="none" stroke-linecap="round" stroke-linejoin="round"/></svg>Unterstützt die nächtliche Regeneration</li>
      <li><svg class="tick" width="24" height="24" viewBox="0 0 24 24"><circle cx="12" cy="12" r="12" fill="#9dc43b"/><path d="M6.5 12.5l3.5 3.5 7.5-8" stroke="#fff" stroke-width="2.6" fill="none" stroke-linecap="round" stroke-linejoin="round"/></svg>Reduziert oxidativen Stress</li>
      <li><svg class="tick" width="24" height="24" viewBox="0 0 24 24"><circle cx="12" cy="12" r="12" fill="#9dc43b"/><path d="M6.5 12.5l3.5 3.5 7.5-8" stroke="#fff" stroke-width="2.6" fill="none" stroke-linecap="round" stroke-linejoin="round"/></svg>Fördert tiefe Erholung</li>
    </ul>

    <div class="count">30</div>
    <div class="count__unit">KAPSELN</div>

    <div class="footer-band">
      <svg class="footer-band__shape" width="540" height="141" viewBox="0 0 540 141">
        <rect x="0" y="47" width="540" height="94" fill="#134a4e"/>
        <path d="M232 141 L262 30 Q270 0 305 0 L540 0 L540 141 Z" fill="#9dc43b"/>
      </svg>
      <div class="intake">
        <svg class="intake__icon" width="17" height="17" viewBox="0 0 34 34"><path d="M20 3a14 14 0 1 0 11 21A12 12 0 0 1 20 3z" fill="#fff"/></svg>
        <span>Abends einnehmen</span>
      </div>
      <div class="complex">
        <div class="complex__title">Abend-Nährstoffkomplex</div>
        <p class="complex__text">Formuliert zur Unterstützung tiefer nächtlicher Reparaturprozesse und zur Förderung gesunder Zellregeneration.</p>
      </div>
    </div>
  </section>

  <section class="lid" aria-label="Deckel Langlebigkeits-Diagnosetest">
    <div class="lid__texture" role="img" aria-label="Dezentes helles Strukturmuster im oberen Deckelbereich"></div>

    <div class="brand">
      <div class="brand__name">Korunelle</div>
      <div class="brand__tagline">Täglicher Baustein Zukunft</div>
    </div>

    <h1 class="lid__title">
      <span class="lid__title-top">LANGLEBIGKEITS</span>
      <span class="lid__title-bottom">DIAGNOSETEST</span>
    </h1>

    <div class="lid__band">
      <svg class="lid__band-shape" width="720" height="228" viewBox="0 0 720 228">
        <path d="M0 228 L0 190 C20 120 50 0 150 0 L720 0 L720 228 Z" fill="#b9d867"/>
        <path d="M14 228 C40 110 70 0 165 0 L720 0 L720 228 Z" fill="#9dc43b"/>
      </svg>
      <p class="lid__claim">Messen, was wirklich zählt. Verstehen Sie<br>Ihr biologisches Alter.</p>
    </div>
  </section>

</body>
</html>
```